Design a leading edge business card for an architectural company

We believe that Velistra Design Collective is redefining the architectural industry. With that, we need a leading edge business card for the company that focuses on landscape architecture, design, and construction.

Our clients are businesses and homeowners so we need a clean, simple, and professional-looking logo. But we want something special. Design must be elegant but unexpected.

Color preferences:
- Preferably with black background but not a must
- Text should be light colored
- Overall, don’t use too much colors.

Content:
- Front of card must contain either just the logo or the logo and business name only.
- Back of card will show the other information (name, title, phone number, email, website, location).

Style:
- Maybe embossing, de-bossing, or spot UV
- Layout should be landscape unless you prove us otherwise.

Size: 1050 x 600 pixels (with 1/8th inch bleed: 1125 x 675 pixels)

Attached is the company logo to incorporate in the design.

```html
<!DOCTYPE html>
<html lang="en">
<head>
<meta charset="utf-8">
<title>Velistra Design Collective – Business Card</title>
<link rel="stylesheet" href="https://fonts.googleapis.com/css2?family=Roboto:wght@400;700&display=swap">
<style>
  :root{
    --page:#e9e9eb;
    --navy-top:#3a3f4e;
    --navy-bottom:#1a1e28;
    --paper:#f4f4f4;
    --accent:#d9362f;
    --ink:#1c202a;
    --light-text:#e6e8ee;
    --muted-text:#b4b8c4;
  }
  *{box-sizing:border-box;margin:0;padding:0}
  html,body{width:1200px;height:912px;overflow:hidden;background:var(--page);font-family:"Roboto",Arial,sans-serif}
  .sheet{position:relative;width:1200px;height:912px}
  .card{position:absolute;top:106px;width:400px;height:700px;overflow:hidden;
    background:linear-gradient(160deg,var(--navy-top) 0%,#262a36 55%,var(--navy-bottom) 100%);
    box-shadow:0 14px 30px rgba(0,0,0,.25)}
  .card--front{left:170px}
  .card--back{left:630px}
  .edge-band{position:absolute;top:0;right:0;width:44px;height:100%;background:var(--paper)}
  .edge-rule{position:absolute;top:0;right:50px;width:4px;height:100%;background:var(--accent)}
  .card--back .edge-band,.card--back .edge-rule{height:330px}
  .brand{position:absolute;left:0;right:44px;text-align:center;color:var(--light-text);font-weight:400}
  .brand__dot{display:block;margin:0 auto 14px;width:34px;height:34px;border-radius:50%;background:var(--light-text)}
  .brand__name{display:block;font-size:30px;letter-spacing:8px}
  .brand__sub{display:block;font-size:10px;letter-spacing:4px;margin-top:6px}
  .card--front .brand{top:250px}
  .card--back .brand{top:60px}
  .card--back .brand__name{font-size:24px;letter-spacing:6px}
  .website{position:absolute;left:34px;bottom:34px;color:var(--light-text);font-size:15px}
  .person{position:absolute;top:210px;left:0;right:44px;text-align:center}
  .person__name{color:#fff;font-weight:700;font-size:24px;letter-spacing:1px}
  .person__title{color:var(--muted-text);font-size:13px;margin-top:6px}
  .contacts{position:absolute;top:330px;left:0;width:100%;list-style:none}
  .contact{display:flex;align-items:center;justify-content:space-between;height:70px;padding:0 30px 0 34px;background:var(--paper);color:var(--ink);font-size:18px}
  .contact + .contact{margin-top:20px}
  .icon{width:36px;height:36px;flex:none}
</style>
</head>
<body>
<main class="sheet">
  <section class="card card--front" aria-label="Card front">
    <div class="edge-rule"></div>
    <div class="edge-band"></div>
    <div class="brand">
      <span class="brand__dot"></span>
      <span class="brand__name">VELISTRA</span>
      <span class="brand__sub">DESIGN COLLECTIVE</span>
    </div>
    <p class="website">www.velistradesign.com</p>
  </section>

  <section class="card card--back" aria-label="Card back">
    <div class="edge-rule"></div>
    <div class="edge-band"></div>
    <div class="brand">
      <span class="brand__dot"></span>
      <span class="brand__name">VELISTRA</span>
      <span class="brand__sub">DESIGN COLLECTIVE</span>
    </div>
    <div class="person">
      <p class="person__name">NAME NAME</p>
      <p class="person__title">Designer</p>
    </div>
    <ul class="contacts">
      <li class="contact"><span>48 Maple St. Hartwell</span>
        <svg class="icon" viewBox="0 0 36 36" aria-hidden="true"><circle cx="18" cy="18" r="18" fill="var(--accent)"/><path d="M10 18 L18 11 L26 18 M13 17 V25 H23 V17" fill="none" stroke="#fff" stroke-width="2.2" stroke-linejoin="round"/></svg></li>
      <li class="contact"><span>+1 555 014 2387</span>
        <svg class="icon" viewBox="0 0 36 36" aria-hidden="true"><circle cx="18" cy="18" r="18" fill="var(--accent)"/><rect x="13" y="9" width="10" height="18" rx="2" fill="none" stroke="#fff" stroke-width="2"/><circle cx="18" cy="24" r="1.2" fill="#fff"/></svg></li>
      <li class="contact"><span>name@velistradesign.com</span>
        <svg class="icon" viewBox="0 0 36 36" aria-hidden="true"><circle cx="18" cy="18" r="18" fill="var(--accent)"/><rect x="9" y="12" width="18" height="12" rx="1.5" fill="none" stroke="#fff" stroke-width="2"/><path d="M9.5 12.5 L18 19 L26.5 12.5" fill="none" stroke="#fff" stroke-width="2"/></svg></li>
      <li class="contact"><span>www.velistradesign.com</span>
        <svg class="icon" viewBox="0 0 36 36" aria-hidden="true"><circle cx="18" cy="18" r="18" fill="var(--accent)"/><circle cx="18" cy="18" r="8.5" fill="none" stroke="#fff" stroke-width="2"/><ellipse cx="18" cy="18" rx="3.5" ry="8.5" fill="none" stroke="#fff" stroke-width="1.6"/><path d="M9.5 18 H26.5" stroke="#fff" stroke-width="1.6"/></svg></li>
    </ul>
  </section>
</main>
</body>
</html>
```